MODELS AGENCY NEW YEAR 2026 CARD

A 10 cm x 21 cm horizontal New Year card for clients of our 2 models agencies, Pommelin (kids) and Velvaride (actors and adults) (logo in the jobs).

Side A of the card: creative mission:
-text: 2026
-text: Peace and Love
-Studio or movie set atmosphere
-tone of voice: optimistic, positive, colorful

Side B:
(name of 4 people of the agency:)
Odette, Anne-Sophie, Hortense & Luc-Antoine,
(2 logos)
Pommelin & VelvaRide
(Adres)
Rue des Tilleuls 74 b3 - 1200 Bruxelles - Belgique

Target Market(s)

Movie directors, photographers

Industry/Entity Type

Fashion, advertising & Movies

Requirements
Must have
• SEE TEXT IN BRIEFING

```html
<!DOCTYPE html>
<html lang="fr">
<head>
<meta charset="utf-8">
<title>Pommelin &amp; Velvaride — New Year 2026</title>
<link rel="stylesheet" href="https://fonts.googleapis.com/css2?family=Abril+Fatface&family=Figtree:wght@400;500&display=swap">
<style>
  :root {
    --backdrop: #3d2d25;
    --blush: #f0e0d6;
    --ink: #3a2a22;
    --rule: #d8c6bb;
    --bronze: #7a4a30;
    --night: #0e0c0b;
    --white: #ffffff;
    --plum: #3f1d5c;
    --orange: #e8561c;
    --sky: #1a9fe0;
  }
  * { margin: 0; padding: 0; box-sizing: border-box; }
  html, body { width: 1200px; height: 1200px; overflow: hidden; }
  body { background: var(--backdrop); position: relative; font-family: "Figtree", sans-serif; }

  .card {
    position: absolute; left: 104px; width: 992px; height: 471px;
    background: var(--blush);
    box-shadow: 0 12px 30px rgba(0,0,0,.35);
    overflow: hidden;
  }
  .card--front { top: 95px; }
  .card--back { top: 635px; }

  /* Front */
  .studio-scene {
    position: absolute; top: 0; right: 0; width: 640px; height: 100%;
    background:
      linear-gradient(180deg, rgba(14,12,11,0) 70%, rgba(90,80,74,.55) 100%),
      linear-gradient(90deg, rgba(240,224,214,0) 0%, rgba(60,50,45,.6) 22%, var(--night) 45%, #2a2420 70%, #6b625c 100%);
  }
  .year-frame {
    position: absolute; left: 76px; top: 66px; width: 180px; height: 343px;
    border: 1px solid var(--ink);
  }
  .year-frame::before, .year-frame::after {
    content: ""; position: absolute; left: 0; right: 0; height: 1px; background: var(--ink);
  }
  .year-frame::before { top: 10px; }
  .year-frame::after { bottom: 10px; }
  .year-stack {
    position: absolute; left: 0; right: 0; top: 34px;
    display: flex; flex-direction: column; align-items: center;
  }
  .year-digits {
    font-family: "Figtree", sans-serif; font-weight: 500;
    font-size: 120px; line-height: 88px; letter-spacing: -2px;
    background: linear-gradient(90deg, var(--bronze) 10%, var(--night) 70%);
    -webkit-background-clip: text; background-clip: text; color: transparent;
  }
  .greeting {
    font-weight: 400; font-size: 42px; line-height: 34px; color: #5a3a28;
    text-align: center; margin: 12px 0 10px; letter-spacing: .5px;
  }

  /* Back */
  .agency-panel {
    position: absolute; top: 0; right: 0; width: 386px; height: 100%;
    background: var(--white);
  }
  .team { position: absolute; left: 67px; top: 92px; width: 424px; list-style: none; }
  .team li {
    font-family: "Abril Fatface", serif; font-size: 40px; color: var(--ink);
    border-bottom: 2px solid var(--rule); line-height: 1; padding: 4px 0 10px; margin-bottom: 6px;
  }
  .address {
    position: absolute; left: 67px; top: 376px;
    font-size: 17px; font-weight: 500; color: var(--ink); letter-spacing: .3px;
  }
  .agency { position: absolute; left: 0; right: 0; text-align: center; color: var(--plum); }
  .agency--adults { top: 95px; }
  .agency--kids { top: 290px; }
  .agency-name { font-family: "Figtree", sans-serif; font-weight: 500; font-size: 38px; line-height: 44px; letter-spacing: 1px; }
  .agency-tagline { font-size: 10px; letter-spacing: 1.6px; margin-top: 6px; }
  .agency-since { font-size: 8px; letter-spacing: .5px; margin-top: 30px; }
</style>
</head>
<body>
  <section class="card card--front">
    <div class="studio-scene" role="img" aria-label="Sepia photograph of a film studio set with crew, cameras and lighting stands"></div>
    <div class="year-frame">
      <div class="year-stack">
        <span class="year-digits">20</span>
        <p class="greeting">PEACE<br>&amp; LOVE</p>
        <span class="year-digits">26</span>
      </div>
    </div>
  </section>

  <section class="card card--back">
    <ul class="team">
      <li>Odette</li>
      <li>Anne-Sophie</li>
      <li>Hortense</li>
      <li>Luc-Antoine</li>
    </ul>
    <p class="address">Rue des Tilleuls 74 b3 - 1200 Bruxelles - Belgique</p>
    <div class="agency-panel">
      <div class="agency agency--adults">
        <div class="agency-name">Velvaride</div>
        <div class="agency-tagline">PEOPLE, ACTORS &amp; MODELS AGENCY</div>
        <div class="agency-since">– SINCE 2000 –</div>
      </div>
      <div class="agency agency--kids">
        <div class="agency-name">Pommelin</div>
        <div class="agency-tagline">CHILDREN MODELS AGENCY</div>
        <div class="agency-since">– SINCE 1982 –</div>
      </div>
    </div>
  </section>
</body>
</html>
```